Menu Revamp- Simplify and highlight

Redesign the current menu while maintaining the existing dimensions to fit within a window display. The goal is to improve readability, declutter the layout, and make price visibility more subtle while ensuring the design remains easy to update annually.

Current Challenges:
• The menu feels cluttered, making it difficult for customers to quickly find what they want.
• Prices stand out too much, drawing more attention than necessary.
• Editing and updating the menu each year is cumbersome and needs simplification.

Requirements:
• Maintain the current specifications and dimensions to ensure it fits in the designated window space.
• Improve readability by organizing the menu in a cleaner, more structured format.
• Adjust the price formatting so it is visible but not the primary focus.
• Ensure the new design allows for easy annual updates, minimizing the need for complete redesigns each year.
• Consider a font and layout that enhance clarity while maintaining the brand’s aesthetic.

Additional Considerations:
• Potential use of color or sectioning to group similar items for better flow.
• A design that aligns with the overall brand identity and customer expectations.
• Digital-friendly formatting for quick edits without affecting the overall structure.

This redesign should make the menu more visually appealing, user-friendly, and practical for future updates while keeping within the original space constraints.
Updates

Gathering more feedback

Target Market(s)

Families and people coming to vacation

Industry/Entity Type

food

Font styles to use
Serif
Sans Serif

Colors
0054AA
0677BA
7BADD7
CADEEF
E8F1F8
F0912C
F2A743
F7CA91
FBE8D2
FDF5EE
EE7325
F08F49
F5BC92
FAE3D3
FDF4ED
EB3D1F
EC4F4E
F09395
F8D3D4
FCEDEE

Requirements
Must have
• all the details, names, and such need to stay. I need it organized better and easier to view and read
Nice to have
• it would be nice if the layers were easier to modify and change year to year.
Should not have
• do not remove details. Please make pricing less prevelant.

```html
<!DOCTYPE html>
<html lang="en">
<head>
<meta charset="utf-8">
<title>Menu Board</title>
<link href="https://fonts.googleapis.com/css2?family=Archivo+Black&family=Poppins:wght@300;400;600;700&family=Roboto+Condensed:wght@400;700&display=swap" rel="stylesheet">
<style>
:root{
  --blue:#1a56ae;
  --sky:#1f9bd7;
  --red:#eb3d1f;
  --orange:#f2a743;
  --gold:#b8892f;
  --line:rgba(255,255,255,.45);
  --white:#ffffff;
}
*{box-sizing:border-box;margin:0;padding:0}
html,body{width:1200px;height:536px;overflow:hidden;background:#ffffff}
body{display:flex;align-items:center;justify-content:center;font-family:"Poppins",sans-serif;color:var(--white)}
.menu{width:716px;height:532px;border:3px solid var(--gold);background:#16233f;display:grid;grid-template-columns:1fr 1fr 1fr;gap:2px}
.col{display:flex;flex-direction:column;overflow:hidden}
.blk{height:var(--h);overflow:hidden;position:relative;flex:none}
.blue{background:var(--blue)}
.sky{background:var(--sky)}
.red{background:var(--red)}
.orange{background:var(--orange)}
.head{display:flex;align-items:center;justify-content:center;font-family:"Archivo Black",sans-serif;font-size:10.5px;letter-spacing:.2px;text-transform:uppercase;border-bottom:1.5px solid rgba(255,255,255,.6)}
.head .hp{font-family:"Roboto Condensed",sans-serif;font-size:5px;margin-left:10px;letter-spacing:0}
.sub{display:flex;align-items:center;justify-content:center;text-align:center;font-size:6.4px;line-height:1.2;padding:0 8px}
.sub.sm{font-size:5.2px}
.item{padding:3px 6px 1px 9px;border-bottom:1px solid var(--line)}
.name{font-size:13px;line-height:1.05;white-space:nowrap}
.name .lt{font-weight:300}
.name .bd{font-weight:700}
.name.mid{font-size:11px;line-height:1}
.desc{font-family:"Roboto Condensed",sans-serif;font-size:4.9px;line-height:1.25;margin-top:1px;max-width:150px}
.price{position:absolute;right:6px;top:6px;font-family:"Roboto Condensed",sans-serif;font-size:4.6px;line-height:10px;text-align:left;opacity:.9}
.tight{padding-top:2px}
.tight .desc{margin-top:0;line-height:1.15}
.ctr{text-align:center;padding:3px 6px;border-bottom:1px solid var(--line)}
.ctr .tt{font-weight:700;font-size:10.5px;line-height:1.1}
.ctr .desc{max-width:none;margin:0 auto}
.kid{display:flex;flex-direction:column;justify-content:center}
.kid .tt{font-size:10px}
.kid .desc{font-size:4.6px}
.kid-last{display:flex;justify-content:center;gap:14px;align-items:center;font-weight:700;font-size:10px}
.shake{text-align:center;padding:4px 8px 2px;border-bottom:1px solid var(--line)}
.shake .tt{font-weight:700;font-size:8.6px;line-height:1.1}
.shake .desc{font-size:5.3px;max-width:none;line-height:1.25}
.shake .price{top:5px;font-size:4.8px}
.sides{display:flex;justify-content:center;align-items:center;gap:6px;font-weight:700;font-size:10px;border-bottom:1px solid rgba(255,255,255,.6)}
.sides small{font-family:"Roboto Condensed",sans-serif;font-weight:400;font-size:4.5px;margin:0 6px 0 2px}
.strip{display:flex;justify-content:center;align-items:center;gap:16px;font-family:"Roboto Condensed",sans-serif;font-size:5.6px}
.flavors{display:grid;grid-template-columns:1fr 1fr;padding:3px 0 0 24px;position:relative}
.flavors::before{content:"";position:absolute;left:50%;top:3px;bottom:3px;width:1px;background:var(--line)}
.flavors ul{list-style:none;font-size:7.2px;line-height:11.3px}
.flavors ul:last-child{padding-left:20px}
.flavors li::before{content:"• "}
</style>
</head>
<body>
<main class="menu">

  <section class="col">
    <h2 class="blk blue head" style="--h:18px">1/4 Hand Smashed Burgers</h2>
    <p class="blk sky sub" style="--h:20px">All of our burgers are 100% hand-smashed ground chuck beef and served on a toasted Artisan bun.</p>
    <div class="blk blue item" style="--h:43px"><div class="name"><span class="lt">The Ledge </span><span class="bd">Cheeseburger</span></div><div class="desc">• Add Bacon or Shredded Brisket - $1.49/$2.49</div><div class="price">Single $ 7.49<br>Double $ +1.99<br>Triple $ +3.98<br>Quad $ +5.97</div></div>
    <div class="blk blue item" style="--h:47px"><div class="name"><span class="lt">Windward </span><span class="bd">Barbecue</span></div><div class="desc">Bacon, Onion Ring, Cheddar Cheese and Jed's® Sassy BBQ Sauce.<br>• Make it Spicy with Jalapenos and Queso - $.99<br>• Add Shredded Brisket - $2.49</div><div class="price">Single $ 7.99<br>Double $ +1.99</div></div>
    <div class="blk blue item" style="--h:32px"><div class="name"><span class="lt">North Meadow </span><span class="bd">Hamburger</span></div><div class="desc">• Add Bacon or Shredded Brisket - $1.49/$2.49</div><div class="price">Single $ 6.99<br>Double $ +1.99</div></div>
    <div class="blk blue item" style="--h:30px"><div class="name mid"><span class="lt">Mel's </span><span class="bd">Avocado Queso</span></div><div class="desc">Avocado, Tomato, and White Queso Cheese</div><div class="price">Single $ 8.99<br>Double $ +1.99</div></div>
    <div class="blk blue item" style="--h:34px"><div class="name mid"><span class="lt">Orchard Town </span><span class="bd">Hot Honey</span></div><div class="desc">Jalapenos, Hot Honey, Pepperjack Cheese,<br>Bacon, Lettuce, Tomato</div><div class="price">Single $ 8.99<br>Double $ +1.99</div></div>
    <div class="blk blue item" style="--h:31px"><div class="name mid"><span class="lt">Sandbar Beach </span><span class="bd">Garlic Parm</span></div><div class="desc">Creamy Garlic Parmesan Sauce, Onion, Lettuce</div><div class="price">Single $ 8.99<br>Double $ +1.99</div></div>
    <div class="blk blue item" style="--h:46px"><div class="name mid"><span class="lt">Warm Creek</span><br><span class="bd">Double Grilled Cheese</span></div><div class="desc">Two Cheesy Patties, a Grilled Cheese Sandwich,<br>and Classic Burger Toppings in One Burger</div><div class="price" style="top:18px">Double $ 10.69</div></div>
    <h2 class="blk red head" style="--h:20px">Sunny Cove Wraps<span class="hp">$ 8.99</span></h2>
    <p class="blk orange sub" style="--h:20px">All wraps are made to order with fresh grilled chicken or shrimp and rolled in a Tomato Tortilla</p>
    <div class="blk red ctr" style="--h:33px"><div class="tt">Avocado Chicken Ranch</div><div class="desc">Smoked Chicken, Bacon, Avocado,<br>Lettuce, Spinach and Tomato with Ranch Dressing</div></div>
    <div class="blk red ctr" style="--h:32px"><div class="tt">BBQ Chicken Bacon</div><div class="desc">Smoked Chicken, Bacon, Cheddar Cheese, Red Onion,<br>Lettuce and Tomato with Jed's Raspberry BBQ Sauce</div></div>
    <div class="blk red ctr" style="--h:33px"><div class="tt">Chipotle Shrimp</div><div class="desc">Fried Shrimp, Tomato and Lettuce with Chili Lime Aioli<br>• Add Avocado or Bacon - $.99 / $1.49 ea</div></div>
    <h2 class="blk blue head" style="--h:18px">Little Anglers (Kids)<span class="hp">$ 7.99</span></h2>
    <p class="blk sky sub" style="--h:10px">Includes Side of Fries or Onion Rings and 12 oz Drink</p>
    <div class="blk blue ctr kid" style="--h:21px"><div class="tt">• Little Burger</div><div class="desc">- Slider size burger with pickles &amp; ketchup. Add cheese for free.</div></div>
    <div class="blk blue ctr kid" style="--h:21px"><div class="tt">• Pulled Pork Sandwich</div><div class="desc">- 1/2 of a regular sandwich with sweet raspberry BBQ sauce.</div></div>
    <div class="blk blue kid-last" style="--h:17px"><span>• Corn Dog</span><span>• Grilled Cheese</span></div>
  </section>

  <section class="col">
    <h2 class="blk red head" style="--h:18px">Pulled Pork &amp; Shrimp</h2>
    <p class="blk orange sub" style="--h:20px">Our Pulled Pork is house smoked and slow roasted.<br>All pork and shrimp are served on a Ciabatta bun.</p>
    <div class="blk red item tight" style="--h:22px"><div class="name mid"><span class="lt">Millrace Pump </span><span class="bd">Pulled Pork</span></div><div class="desc">Pulled Pork and Jed's® Sweet Raspberry BBQ Sauce</div><div class="price" style="top:4px">Double $ 8.49</div></div>
    <div class="blk red item tight" style="--h:22px"><div class="name mid"><span class="lt">Second Bend </span><span class="bd">Sweet Pulled Pork</span></div><div class="desc">Pulled Pork, Jed's® Sweet Raspberry BBQ Sauce and Coleslaw</div><div class="price" style="top:4px">Double $ 8.49</div></div>
    <div class="blk red item tight" style="--h:28px"><div class="name mid"><span class="lt">First Bend </span><span class="bd">Spicy Pulled Pork</span></div><div class="desc">Pulled Pork, Jed's® Sassy BBQ Sauce,<br>Chopped Bacon, Pepperjack Cheese and Jalapenos</div><div class="price" style="top:4px">Double $ 8.99</div></div>
    <div class="blk red item tight" style="--h:29px"><div class="name mid"><span class="lt">Gull Harbor </span><span class="bd">Shrimp Po' Boy</span></div><div class="desc">Fried Shrimp, Tomato and Lettuce with Chili Lime Aioli<br>• Add Avocado or Bacon - $.99 / $1.49 ea</div><div class="price" style="top:8px">Double $ 8.99</div></div>
    <h2 class="blk blue head" style="--h:18px">Shredded Brisket</h2>
    <p class="blk sky sub" style="--h:21px">Our Shredded Brisket is smoked, braised, and shredded.<br>Served on Ciabatta Buns.</p>
    <div class="blk blue item tight" style="--h:21px"><div class="name mid"><span class="lt">Millrace Pump </span><span class="bd">Brisket</span></div><div class="desc">Brisket and Jed's® Sweet Raspberry BBQ Sauce</div><div class="price" style="top:4px">Double $ 9.99</div></div>
    <div class="blk blue item tight" style="--h:21px"><div class="name mid"><span class="lt">Second Bend </span><span class="bd">Sweet Brisket</span></div><div class="desc">Brisket, Jed's® Sweet Raspberry BBQ Sauce and Coleslaw</div><div class="price" style="top:4px">Double $ 9.99</div></div>
    <div class="blk blue item tight" style="--h:31px"><div class="name mid"><span class="lt">First Bend </span><span class="bd">Spicy Brisket</span></div><div class="desc">Brisket, Jed's® Sassy BBQ Sauce, Chopped Bacon,<br>Pepperjack Cheese and Jalapenos</div><div class="price" style="top:4px">Double $ 10.99</div></div>
    <h2 class="blk red head" style="--h:18px;font-size:9.5px">Driftwood Beach Loaded Fries<span class="hp">$ 7.99</span></h2>
    <p class="blk orange sub" style="--h:31px">Shoreline Fries with Pulled Pork, Bacon,<br>Tomatoes, Onion, and Jalapenos smothered<br>in White Queso and BBQ Sauce.</p>
    <p class="blk red sub sm" style="--h:8px">• Substitute Pork for Shredded Brisket - $2.99</p>
    <h2 class="blk blue head" style="--h:19px">Fresh Meadow Salads<span class="hp">$ 9.99</span></h2>
    <div class="blk blue ctr" style="--h:41px"><div class="tt">Sunrise Apple</div><div class="desc">Chopped Apples, Candied Walnuts, Red Onion and<br>Feta Cheese on Fresh Spinach and Lettuce Medley.<br>• Best with Jed's® Raspberry Vinaigrette.<br>• Add Chicken Breast - $1.00</div></div>
    <div class="blk blue ctr" style="--h:37px"><div class="tt">Tall Pines Chicken Avocado</div><div class="desc">Smoked Chicken, Crumbled Bacon, Avocado, Red Onion<br>and Diced Tomatoes on Lettuce Medley.<br>• Best with Ranch Dressing</div></div>
    <div class="blk blue ctr" style="--h:35px"><div class="tt">Sunset Bacon</div><div class="desc">Pulled Pork, Crumbled Bacon, Candied Walnuts, Feta Cheese<br>and Red Onion on Spinach and Lettuce Medley.<br>• Best with Ranch Dressing</div></div>
    <h2 class="blk red head" style="--h:21px">Sides</h2>
    <div class="blk red sides" style="--h:22px">Shoreline Fries<small>$ 4.99</small>Onion Rings<small>$ 5.69</small></div>
    <div class="blk red sides" style="--h:22px">Creamy Coleslaw<small>$ 3.99</small>Side Salad<small>$ 3.99</small></div>
    <div class="blk red sides" style="--h:21px;border:0">Mac n Cheese Bites<small>$ 5.29</small></div>
  </section>

  <section class="col">
    <h2 class="blk blue head" style="--h:18px;border:0">Shakes</h2>
    <h3 class="blk sky head" style="--h:13px;font-family:'Poppins',sans-serif;font-weight:700;font-size:8px;border:0">Monster Style</h3>
    <p class="blk blue sub" style="--h:38px;font-size:6.6px;border-bottom:1px solid var(--line)">Our Monster Shakes start with our thick and creamy soft serve ice cream. We blend in handcrafted ingredients and top with whipped cream and other treats for a Monster taste!<br>Sold as large only</p>
    <div class="blk blue shake" style="--h:33px"><div class="tt">• Jed's Jammin' Raspberry</div><div class="desc">Made with double raspberries and topped<br>with Jed's Raspberry Jam and whipped cream.</div><div class="price">$ 6.99</div></div>
    <div class="blk blue shake" style="--h:32px"><div class="tt">• Apple Pie à la Mode</div><div class="desc">An entire slice of Apple Pie blended with caramel<br>and topped with whipped cream and caramel.</div><div class="price">$ 8.99</div></div>
    <div class="blk blue shake" style="--h:32px"><div class="tt">• Cocoa Crunch Big Scoop</div><div class="desc">A double scoop of cocoa crunch cookies &amp; vanilla wafers<br>and topped with a Big Scoop and whipped cream.</div><div class="price">$ 6.99</div></div>
    <div class="blk blue shake" style="--h:32px"><div class="tt">• PB Cup PB Chocolate Cake</div><div class="desc">PB cups blended into our rich ice cream. And because we can, we add<br>an entire slice of PB Cup Chocolate Cake on top. With whipped cream.</div><div class="price">$ 6.99</div></div>
    <div class="blk blue shake" style="--h:39px"><div class="tt">• Raspberry Cheesecake Cheesecake</div><div class="desc">Real raspberries blended with chunks of cheesecake.<br>Topped with an entire piece of Raspberry<br>Cheesecake and whipped cream.</div><div class="price">$ 9.99</div></div>
    <div class="blk blue shake" style="--h:31px;border-bottom:2px solid #fff"><div class="tt">• Cookie Cookie Dough</div><div class="desc">A double scoop of cookie dough chunks and topped<br>with a chocolate chip cookie and whipped cream.</div><div class="price">$ 6.99</div></div>
    <h2 class="blk red head" style="--h:16px;border:0">Classic</h2>
    <div class="blk orange strip" style="--h:11px;border-bottom:1px solid rgba(255,255,255,.5)"><span>Whipped Cream &nbsp;$ 0.49</span><span>Small - &nbsp;$ 4.99</span><span>Large - &nbsp;$ 6.49</span></div>
    <p class="blk orange sub" style="--h:29px;font-size:6px">Our Classic Shakes are made with extra creamy soft serve and served in environmental friendly cups. Shake flavors are as listed.<br>No exceptions or combinations.</p>
    <div class="blk red flavors" style="--h:199px">
      <ul>
        <li>Famous Raspberry</li><li>Raspberry Cheesecake</li><li>Raspberry Cocoa Crunch</li><li>Raspberry Piña Colada</li><li>Raspberry Brownie</li><li>Raspberry Hazelnut Swirl</li><li>Raspberry Sugar Cookie</li><li>Raspberry Cookie Dough</li><li>Raspberry Marshmallow</li><li>Strawberry</li><li>Strawberry Cheesecake</li><li>Strawberry Cocoa Crunch</li><li>Strawberry Brownie</li><li>Strawberry Hazelnut Swirl</li><li>Strawberry Marshmallow</li><li>Strawberry Cookie</li><li>Strawberry Chocolate</li>
      </ul>
      <ul>
        <li>Piña Colada</li><li>Caramel</li><li>S'mores</li><li>Brownie</li><li>Chocolate Brownie</li><li>Hazelnut Brownie</li><li>Caramel Brownie</li><li>Caramel Cookie</li><li>Chocolate</li><li>Cocoa Crunch</li><li>Cookie Dough</li><li>Marshmallow</li><li>Hazelnut Swirl</li><li>Nutty Bar</li><li>Peanut Cup</li><li>Spice Cookie</li>
      </ul>
    </div>
  </section>

</main>
</body>
</html>
```